Business cards

I would like a black background with the design I previously chose. I need 2 sets of cards. Mine will have Rosalind Pickett, Broker/Owner, 307-484-2176 and rosalind.brightmeadow@mailvista.test
The second set will read, Corey Vandelow, Realtor 307-538-7042, corey.brightmeadow@mailvista.test

```html
<!DOCTYPE html>
<html lang="en">
<head>
<meta charset="UTF-8">
<title>Business Cards – Rosalind Pickett &amp; Corey Vandelow</title>
<link rel="stylesheet" href="https://fonts.googleapis.com/css2?family=Oswald:wght@500;600&family=Roboto:wght@500&display=swap">
<style>
  :root {
    --page: #e8e8e8;
    --card: #050505;
    --name-green: #52c46d;
    --title-green: #3f9f58;
    --map-green: #1b5a30;
    --contact: #f4f4f4;
  }
  * { margin: 0; padding: 0; box-sizing: border-box; }
  html, body {
    width: 800px; height: 1200px; overflow: hidden;
    background: var(--page);
  }
  .canvas { position: relative; width: 800px; height: 1200px; }
  .business-card {
    position: absolute; left: 50px;
    width: 700px; height: 400px;
    background: var(--card);
    overflow: hidden;
    box-shadow: 0 8px 22px rgba(0,0,0,0.25);
  }
  .card-realtor { top: 110px; }
  .card-owner { top: 690px; }

  .world-map-area {
    position: absolute; left: 110px; top: 30px;
    width: 560px; height: 320px;
    background: radial-gradient(ellipse at 55% 45%, var(--map-green) 0%, rgba(27,90,48,0.45) 45%, rgba(5,5,5,0) 75%);
    opacity: 0.75;
  }

  .name-block { position: absolute; }
  .card-realtor .name-block { left: 150px; top: 42px; }
  .card-owner .name-block { right: 30px; top: 146px; }

  .holder-name {
    font-family: 'Oswald', sans-serif;
    font-weight: 600;
    font-size: 42px;
    color: var(--name-green);
    text-transform: uppercase;
    line-height: 1;
    white-space: nowrap;
  }
  .holder-title {
    font-family: 'Oswald', sans-serif;
    font-weight: 500;
    font-size: 26px;
    color: var(--title-green);
    line-height: 1;
    margin-top: 2px;
    white-space: nowrap;
  }
  .card-owner .holder-title { letter-spacing: 8px; }

  .contact-list {
    position: absolute; left: 56px; top: 240px;
    list-style: none;
    font-family: 'Roboto', sans-serif;
    font-weight: 500;
    color: var(--contact);
    font-size: 26px;
  }
  .contact-item {
    display: flex; align-items: center; gap: 16px;
    height: 46px;
    white-space: nowrap;
  }
  .contact-icon { width: 22px; height: 22px; flex: none; }
</style>
</head>
<body>
<main class="canvas">

  <section class="business-card card-realtor">
    <div class="world-map-area" role="img" aria-label="Dotted world map in green"></div>
    <div class="name-block">
      <h1 class="holder-name">Corey Vandelow</h1>
      <p class="holder-title">Realtor</p>
    </div>
    <ul class="contact-list">
      <li class="contact-item">
        <svg class="contact-icon" viewBox="0 0 24 24" aria-hidden="true"><path fill="#f4f4f4" d="M6.6 10.8a15 15 0 0 0 6.6 6.6l2.2-2.2c.3-.3.7-.4 1-.2 1.1.4 2.3.6 3.6.6.6 0 1 .4 1 1V20c0 .6-.4 1-1 1A17 17 0 0 1 3 4c0-.6.4-1 1-1h3.5c.6 0 1 .4 1 1 0 1.3.2 2.5.6 3.6.1.3 0 .7-.2 1z"/></svg>
        <span class="contact-phone">307-538-7042</span>
      </li>
      <li class="contact-item">
        <svg class="contact-icon" viewBox="0 0 24 24" aria-hidden="true"><rect x="2" y="5" width="20" height="14" rx="1.5" fill="#f4f4f4"/><path d="M3 6l9 7 9-7" fill="none" stroke="#050505" stroke-width="1.6"/></svg>
        <span class="contact-email">corey.brightmeadow@mailvista.test</span>
      </li>
    </ul>
  </section>

  <section class="business-card card-owner">
    <div class="world-map-area" role="img" aria-label="Dotted world map in green"></div>
    <div class="name-block">
      <h1 class="holder-name">Rosalind Pickett</h1>
      <p class="holder-title">Broker/Owner</p>
    </div>
    <ul class="contact-list">
      <li class="contact-item">
        <svg class="contact-icon" viewBox="0 0 24 24" aria-hidden="true"><path fill="#f4f4f4" d="M6.6 10.8a15 15 0 0 0 6.6 6.6l2.2-2.2c.3-.3.7-.4 1-.2 1.1.4 2.3.6 3.6.6.6 0 1 .4 1 1V20c0 .6-.4 1-1 1A17 17 0 0 1 3 4c0-.6.4-1 1-1h3.5c.6 0 1 .4 1 1 0 1.3.2 2.5.6 3.6.1.3 0 .7-.2 1z"/></svg>
        <span class="contact-phone">307-484-2176</span>
      </li>
      <li class="contact-item">
        <svg class="contact-icon" viewBox="0 0 24 24" aria-hidden="true"><rect x="2" y="5" width="20" height="14" rx="1.5" fill="#f4f4f4"/><path d="M3 6l9 7 9-7" fill="none" stroke="#050505" stroke-width="1.6"/></svg>
        <span class="contact-email">rosalind.brightmeadow@mailvista.test</span>
      </li>
    </ul>
  </section>

</main>
</body>
</html>
```